Presentation card Launchpad KOVA - Tech Incubator from Perú

We need a Design to promote the incubator of technology Startups.
We are in Perú, we work with a string tech filter and develop enterprenurship competencies in the Startup team.
The card is to facilitators and staff memebers of LaunchpadKOVA.
We want a clear, modern, tech and agile Design.

We work to help New enterprises of technology here in Perú, we expect the candidates have a big competencies to Research and develop technological products.

We work using methodologies from QRB, Felstrom, Bellcourt and London univeesities. Our book base is The arte of the venturer.

We work events all year using diferent formats: Gridvane, Marlow prize, OTRV Plan Challenge you can use these logros in your Design.

Set the name, role, email, cell phone number, address.

Example:
// Contact info section
Osvaldo Quintanar
Rapid Prototyping Center Manager
osvaldo.quintanar@kova.edu.pe
(511) 988 437 216

// Address info section
LaunchpadKOVA
Technology-based business incubator
Av. Los Cedrales 475, Surquillo
Lima - Perú
web: launchpad-kova.org.pe
email: launchpad@kova.edu.pe
phone number: (511) 3692548 ext. 4186

// (optional)Lema section
Making happy using technology

// Social network section
facebook: launchpadkovaoficial

Target Market(s)

Enterprenurship, CTO, Investors, Companies interested on open innovation services

Industry/Entity Type

Information Technology

Contact Information for Business Card

Name, Role, Email, Cell phone number

Colors

Designer to choose colors to be used in the design.

Requirements
Must have
• Logo forms and colors
Nice to have
• I add pictures of the leaders of incubator
Should not have
• No vertical designs

```html
<!DOCTYPE html>
<html lang="en">
<head>
<meta charset="utf-8">
<title>Launchpad KOVA – Business Card</title>
<link rel="stylesheet" href="https://fonts.googleapis.com/css2?family=Open+Sans:wght@400;700&display=swap">
<style>
  :root {
    --backdrop: #3a3b3e;
    --card-white: #ffffff;
    --card-dark: #2a2a2c;
    --ink: #231f20;
    --ink-soft: #3b3b3d;
    --magenta: #b8285a;
    --paper-white: #f7f7f7;
  }
  * { margin: 0; padding: 0; box-sizing: border-box; }
  html, body {
    width: 1200px; height: 1000px; overflow: hidden;
    background: var(--backdrop);
    font-family: "Open Sans", Arial, sans-serif;
  }
  .stage {
    position: relative; width: 1200px; height: 1000px;
    display: flex; flex-direction: column; align-items: center; justify-content: center; gap: 44px;
  }
  .card {
    position: relative; width: 700px; height: 400px; overflow: hidden;
    box-shadow: 0 10px 28px rgba(0,0,0,.35);
  }
  .card--back { background: var(--card-dark); display: flex; align-items: center; justify-content: center; }
  .card--front { background: var(--card-white); }

  .brand { display: flex; align-items: center; gap: 14px; }
  .brand__mark { width: 26px; height: 26px; background: var(--magenta); }
  .brand__name { font-weight: 700; text-transform: uppercase; letter-spacing: .5px; line-height: 1; }
  .card--back .brand__name { color: var(--paper-white); font-size: 52px; }
  .card--back .brand__mark { width: 40px; height: 40px; }
  .card--front .brand { position: absolute; left: 54px; top: 70px; }
  .card--front .brand__name { color: var(--ink); font-size: 36px; }

  .contact { position: absolute; left: 54px; bottom: 70px; list-style: none; }
  .contact__item { display: flex; align-items: center; gap: 10px; font-size: 17px; color: var(--ink-soft); line-height: 1.45; }
  .contact__icon { width: 16px; height: 16px; flex: none; }

  .person { position: absolute; right: 58px; bottom: 56px; text-align: right; }
  .person__name { color: var(--magenta); font-weight: 700; font-size: 23px; margin-bottom: 4px; }
  .person__role, .person__place { color: var(--ink-soft); font-size: 19px; line-height: 1.2; }

  .edge-tab { position: absolute; right: 0; bottom: 60px; width: 16px; }
  .edge-tab__accent { height: 26px; background: var(--magenta); }
  .edge-tab__base { height: 56px; background: var(--ink); }
</style>
</head>
<body>
<main class="stage">
  <section class="card card--back" aria-label="Card back">
    <div class="brand">
      <span class="brand__name">Launchpad KOVA</span>
      <span class="brand__mark"></span>
    </div>
  </section>

  <section class="card card--front" aria-label="Card front">
    <div class="brand">
      <span class="brand__name">Launchpad KOVA</span>
      <span class="brand__mark"></span>
    </div>

    <ul class="contact">
      <li class="contact__item">
        <svg class="contact__icon" viewBox="0 0 16 16" aria-hidden="true">
          <rect x="3.5" y="0.8" width="9" height="14.4" rx="1.6" fill="none" stroke="var(--magenta)" stroke-width="1.8"/>
          <rect x="6.5" y="12" width="3" height="1.4" fill="var(--magenta)"/>
        </svg>
        742-519-0386
      </li>
      <li class="contact__item">
        <svg class="contact__icon" viewBox="0 0 16 16" aria-hidden="true">
          <rect x="0.5" y="3" width="15" height="10" fill="var(--magenta)"/>
          <path d="M0.8 3.4 L8 9 L15.2 3.4" fill="none" stroke="#fff" stroke-width="1.3"/>
        </svg>
        osvaldo@launchpadkova.com
      </li>
    </ul>

    <div class="person">
      <p class="person__name">Osvaldo Quintanar</p>
      <p class="person__role">Senior Software</p>
      <p class="person__role">Development Engineer</p>
      <p class="person__place">Peru</p>
    </div>

    <div class="edge-tab" aria-hidden="true">
      <div class="edge-tab__accent"></div>
      <div class="edge-tab__base"></div>
    </div>
  </section>
</main>
</body>
</html>
```